Brom-leigh Sky Harbour Custom Brokers Limited

Shop online from the USA and Ship to Jamaica
Customs Brokerage, Import Export and logistic Services
Address:- 238-240 Halden Brook Road Kingston Jamaica
Email: info@bromleighskyharbour,com
Web: www.bromleighskyharbour.com
Telephone: (876) 555-0148, (876) 555-0193
flyer should be quarter page must print information on back and front

```html
<!DOCTYPE html>
<html lang="en">
<head>
<meta charset="utf-8">
<title>Brom-leigh Sky Harbour Custom Brokers – Shop Online Flyer</title>
<link rel="stylesheet" href="https://fonts.googleapis.com/css2?family=Montserrat:wght@300;400;500;600;700;800&display=swap">
<style>
  :root {
    --navy: #0f2a52;
    --gold: #efab0f;
    --gold-light: #f6c64a;
    --ink: #1d2330;
    --muted: #8a8f99;
    --white: #ffffff;
    --stage: #e4e4e4;
    --rule: #c9ccd3;
  }
  * { margin: 0; padding: 0; box-sizing: border-box; }
  html, body {
    width: 1200px; height: 1200px; overflow: hidden;
    background: var(--stage);
    font-family: "Montserrat", sans-serif;
  }
  .flyer {
    position: absolute; left: 180px; top: 57px;
    width: 840px; height: 1086px;
    background: var(--white);
    overflow: hidden;
    box-shadow: 0 4px 14px rgba(0,0,0,0.18);
  }
  .top-band {
    position: absolute; left: 0; top: 0; width: 840px; height: 38px;
    background: linear-gradient(90deg, rgba(239,171,15,0) 0%, rgba(239,171,15,0.15) 35%, var(--gold-light) 80%, var(--gold) 100%);
  }
  .hero-photo {
    position: absolute; left: 0; top: 0; width: 520px; height: 730px;
    background:
      linear-gradient(90deg, rgba(255,255,255,0) 55%, #ffffff 100%),
      linear-gradient(180deg, #f3dcc4 0%, #d9a35a 40%, #e8b22a 70%, #dcdcdc 100%);
  }
  .brand {
    position: absolute; left: 380px; top: 112px; width: 420px;
    text-align: center; color: var(--navy);
  }
  .brand-mark {
    display: block; width: 70px; height: 70px; margin: 0 auto 36px;
    border-radius: 50%; background: var(--navy);
  }
  .brand-name { font-size: 23px; font-weight: 700; letter-spacing: 0.3px; line-height: 1.2; }
  .brand-sub {
    font-size: 14px; font-weight: 400; letter-spacing: 5px;
    color: var(--muted); margin-top: 4px;
  }
  .headline {
    position: absolute; left: 422px; top: 330px;
    color: var(--gold); font-weight: 800;
    font-size: 84px; line-height: 68px; letter-spacing: -1px;
  }
  .subhead {
    position: absolute; left: 422px; top: 470px;
    color: var(--navy); font-weight: 600;
    font-size: 37px; line-height: 40px;
  }
  .divider {
    position: absolute; left: 422px; top: 573px; width: 350px; height: 1px;
    background: var(--rule);
  }
  .services {
    position: absolute; left: 422px; top: 594px;
    color: var(--ink); font-weight: 400;
    font-size: 23px; line-height: 31px; letter-spacing: 0.5px;
  }
  .logistics-photo {
    position: absolute; left: 0; top: 730px; width: 421px; height: 356px;
    background: linear-gradient(180deg, #b9a98f 0%, #e8b870 45%, #c2643a 75%, #5a4a45 100%);
  }
  .contact-panel {
    position: absolute; left: 421px; top: 730px; width: 419px; height: 345px;
    background: var(--navy); color: var(--white);
  }
  .bottom-band {
    position: absolute; left: 0; bottom: 0; width: 840px; height: 11px;
    background: var(--gold);
  }
  .contact-row { position: absolute; left: 81px; white-space: nowrap; }
  .contact-icon { position: absolute; left: -58px; }
  .address { top: 78px; font-size: 20px; line-height: 26px; font-weight: 500; }
  .online { top: 143px; font-size: 17px; line-height: 26px; font-weight: 600; }
  .phones { top: 210px; font-size: 35px; line-height: 40px; font-weight: 700; color: var(--gold); }
</style>
</head>
<body>
  <main class="flyer">
    <div class="hero-photo" role="img" aria-label="Smiling woman in a yellow sweater shopping on a laptop"></div>
    <div class="top-band"></div>

    <div class="brand">
      <span class="brand-mark"></span>
      <div class="brand-name">BROM-LEIGH SKY HARBOUR</div>
      <div class="brand-sub">Custom Brokers Ltd.</div>
    </div>

    <h1 class="headline">SHOP<br>ONLINE</h1>
    <p class="subhead">From the USA and<br>Ship to Jamaica</p>
    <div class="divider"></div>
    <p class="services">Customs Brokerage, Import<br>Export and logistic Services</p>

    <div class="logistics-photo" role="img" aria-label="Cargo plane over shipping containers, port cranes and trucks at sunset"></div>

    <section class="contact-panel">
      <div class="contact-row address">
        <svg class="contact-icon" width="30" height="38" viewBox="0 0 30 38" style="top:2px">
          <path d="M15 0C6.7 0 0 6.5 0 14.6 0 25 15 38 15 38s15-13 15-23.4C30 6.5 23.3 0 15 0z" fill="#efab0f"/>
          <circle cx="15" cy="14" r="5.5" fill="#0f2a52"/>
        </svg>
        238-240 Halden Brook Road<br>Kingston, Jamaica
      </div>
      <div class="contact-row online">
        <svg class="contact-icon" width="30" height="40" viewBox="0 0 30 40" style="top:4px">
          <circle cx="17" cy="13" r="10" fill="none" stroke="#efab0f" stroke-width="3"/>
          <circle cx="17" cy="13" r="4" fill="none" stroke="#efab0f" stroke-width="3"/>
          <path d="M11 21 L3 38 M11 21 L14 32" fill="none" stroke="#efab0f" stroke-width="3" stroke-linecap="round"/>
        </svg>
        info@bromleighskyharbour,com<br>www.bromleighskyharbour.com
      </div>
      <div class="contact-row phones">
        <svg class="contact-icon" width="28" height="66" viewBox="0 0 28 66" style="top:6px">
          <path d="M20 2 L10 2 C5 2 2 6 2 12 L2 54 C2 60 5 64 10 64 L20 64 L20 50 L13 50 L13 16 L20 16 Z" fill="#ffffff"/>
        </svg>
        (876) 555-0148<br>(876) 555-0193
      </div>
    </section>
    <div class="bottom-band"></div>
  </main>
</body>
</html>
```